I am a pastry chef and just started my own business. I make all sorts of pastries: french macarons, petit fours, artisan chocolates, artisan bread, and they can be ordered on the website. I'm obsessed with Wonderland, so I'd like to have a logo & a background that incorporate that, something whimsical. I was thinking of a white rabbit wearing a chef toque - maybe he could have a monocle on. The logo could go on one side of the business card with "Tiny Baker of Moonbrook" on a banner of some sort at the bottom, and the contact & info could go on the other side. I'd like a really light color as the background, maybe a really light yellow.

Industry/Entity Type

Chef

Contact Information for Business Card

Tiny Baker of Moonbrook
Mira Delsan Corwick
tinybakerofmoonbrook.shopveltra.com
tinybakerofmoonbrook@mailquor.com
514-83-2071

```html
<!DOCTYPE html>
<html lang="en">
<head>
<meta charset="utf-8">
<title>Tiny Baker of Moonbrook — Business Cards</title>
<link href="https://fonts.googleapis.com/css2?family=Patrick+Hand&display=swap" rel="stylesheet">
<style>
  :root {
    --backdrop: #e9e6e2;
    --card: #000000;
    --ink: #ffffff;
    --ink-soft: #e6e6e6;
  }
  * { margin: 0; padding: 0; box-sizing: border-box; }
  html, body { width: 1200px; height: 848px; overflow: hidden; }
  body {
    background: var(--backdrop);
    font-family: "Patrick Hand", "Comic Sans MS", cursive;
    color: var(--ink);
    position: relative;
  }
  .card {
    position: absolute;
    width: 620px;
    height: 354px;
    background: var(--card);
    border-radius: 26px;
    box-shadow: 0 10px 26px rgba(0,0,0,0.28);
    overflow: hidden;
  }
  .card--info { left: 60px; top: 50px; }
  .card--brand { left: 520px; top: 444px; }

  .brand-mark {
    position: absolute;
    background: var(--ink);
    border-radius: 50%;
  }
  .card--info .brand-mark { left: 150px; top: 64px; width: 92px; height: 92px; }
  .card--brand .brand-mark { left: 140px; top: 128px; width: 150px; height: 150px; }

  .business-name {
    position: absolute;
    font-size: 30px;
    font-weight: 400;
    line-height: 1;
    white-space: nowrap;
  }
  .owner-name {
    position: absolute;
    font-size: 19px;
    line-height: 1;
    color: var(--ink-soft);
    white-space: nowrap;
  }
  .card--info .business-name { left: 262px; top: 66px; }
  .card--info .owner-name { right: 108px; top: 104px; }
  .card--brand .business-name { right: 40px; top: 116px; font-size: 30px; }
  .card--brand .owner-name { right: 40px; top: 156px; }

  .contact-list {
    position: absolute;
    right: 42px;
    top: 196px;
    list-style: none;
    text-align: right;
    font-size: 21px;
    line-height: 1.22;
  }
  .contact-list li { display: flex; justify-content: flex-end; align-items: center; gap: 10px; }
  .contact-icon { width: 16px; height: 16px; flex: none; }
</style>
</head>
<body>

  <section class="card card--info" aria-label="Contact side">
    <div class="brand-mark" aria-hidden="true"></div>
    <h1 class="business-name">Tiny Baker of Moonbrook</h1>
    <p class="owner-name">Mira Delsan Corwick</p>
    <ul class="contact-list">
      <li>514-83-2071
        <svg class="contact-icon" viewBox="0 0 16 16" aria-hidden="true"><path d="M3.5 1.5l2.5 0 1 3.5-1.6 1.2c.8 1.7 2 2.9 3.6 3.7l1.2-1.6 3.5 1v2.5c0 .9-.7 1.6-1.6 1.6C6.6 13.4 2.6 9.4 1.9 3.1c0-.9.7-1.6 1.6-1.6z" fill="#fff"/></svg>
      </li>
      <li>tinybakerofmoonbrook.shopveltra.com
        <svg class="contact-icon" viewBox="0 0 16 16" aria-hidden="true"><circle cx="8" cy="8" r="6.5" fill="none" stroke="#fff" stroke-width="1.5"/><ellipse cx="8" cy="8" rx="2.8" ry="6.5" fill="none" stroke="#fff" stroke-width="1.2"/><line x1="1.5" y1="8" x2="14.5" y2="8" stroke="#fff" stroke-width="1.2"/></svg>
      </li>
      <li>tinybakerofmoonbrook@mailquor.com
        <svg class="contact-icon" viewBox="0 0 16 16" aria-hidden="true"><rect x="1.5" y="3.5" width="13" height="9" fill="none" stroke="#fff" stroke-width="1.4"/><path d="M1.5 3.5L8 9l6.5-5.5" fill="none" stroke="#fff" stroke-width="1.4"/></svg>
      </li>
    </ul>
  </section>

  <section class="card card--brand" aria-label="Brand side">
    <div class="brand-mark" aria-hidden="true"></div>
    <h2 class="business-name">Tiny Baker of Moonbrook</h2>
    <p class="owner-name">Mira Delsan Corwick</p>
  </section>

</body>
</html>
```